Container Web Design Project

I need the front page of my website to have a new, fresh look.
Our company is a highly specialized marketplace for shipping containers (yes, the 20' and 40' kind). Basically, think of Lokko for shipping containers.
I have all of the links/content that I need plugged into a wireframe (attached), and the core color (blue #0073a2) of our existing site should stay the same as we've got stationary, business cards, marketing materials...
If you have any questions please ask.

```html
<!DOCTYPE html>
<html lang="en">
<head>
<meta charset="utf-8">
<title>BoxBid.com — Shipping Container Marketplace</title>
<link rel="stylesheet" href="https://fonts.googleapis.com/css2?family=Open+Sans:wght@400;600;700&family=Ubuntu+Condensed&display=swap">
<style>
:root{
  --brand:#0073a2;
  --bg-deep:#064a72;
  --bg-mid:#0a6b98;
  --navy:#0b4468;
  --ink:#333;
  --muted:#555;
  --line:#d8d8d8;
  --panel:#f3f3f3;
  --green:#6aa63a;
  --heading:#0c5d8a;
}
*{box-sizing:border-box;margin:0;padding:0}
html,body{width:1200px;height:1000px;overflow:hidden}
body{font-family:"Open Sans",Arial,sans-serif;color:var(--ink);
  background:radial-gradient(ellipse at 50% 30%,#0d7bab 0%,var(--bg-mid) 45%,var(--bg-deep) 100%);position:relative}
.abs{position:absolute}
.deco{position:absolute;background:linear-gradient(180deg,#1178a8,#0a5d88);opacity:.7}
.logo{left:240px;top:18px;width:198px;height:44px;border:2px solid #fff;border-radius:4px;background:var(--navy);
  color:#fff;font-family:"Ubuntu Condensed",sans-serif;font-size:30px;line-height:38px;text-align:center}
.toplinks{right:244px;top:31px;color:#fff;font-size:11px}
.toplinks span{margin:0 5px}
.mainnav{left:240px;top:79px;width:719px;height:34px;border-radius:4px;background:linear-gradient(#fff,#e4e4e4)}
.mainnav a{position:absolute;top:4px;font-size:10px;letter-spacing:-.2px;color:#222;text-decoration:none;height:26px;line-height:26px;white-space:nowrap}
.mainnav a.active{left:4px;width:134px;background:var(--navy);color:#fff;border-radius:3px;text-align:center}
.search{top:127px;height:29px;border-radius:15px;background:#0a4c73;border:1px solid #3a86b2;color:#fff;font-size:8.5px;line-height:27px}
.search-input{left:240px;width:421px;padding-left:39px}
.select{padding-left:16px}
.select::after{content:"";position:absolute;right:10px;top:12px;border:4px solid transparent;border-top-color:#fff}
.search-btn{left:857px;width:103px;background:linear-gradient(#fff,#dcdcdc);border:none;color:var(--heading);font-weight:700;font-size:12px;text-align:center}
.content{left:229px;top:167px;width:742px;height:860px;background:#fff;border-radius:6px}
.divider{left:430px;top:176px;width:1px;height:830px;background:#e6e6e6}
.sidemenu{left:240px;top:174px;width:175px;list-style:none}
.sidemenu li{height:31.5px;line-height:30px;border-bottom:1px solid #ddd;font-size:10px;font-weight:600;color:#444;padding-left:13px;position:relative;white-space:nowrap}
.sidemenu li::before{content:"";position:absolute;left:1px;top:12px;border:3px solid transparent;border-left:4px solid #666}
.sidemenu li:last-child{border-bottom:none}
.side-title{left:240px;font-size:13px;letter-spacing:-.4px;font-weight:700;color:var(--heading);white-space:nowrap}
.newsletter{left:240px;top:478px;width:178px;height:30px;border:1px solid #ddd;font-size:8px;line-height:28px;padding-left:9px}
.newsletter b{position:absolute;right:5px;top:6px;height:17px;line-height:17px;padding:0 7px;background:var(--navy);color:#fff;border-radius:2px;font-size:8px}
.banner{left:240px;top:523px;width:177px;height:118px;border:1px solid #ccc;background:#eee;padding:5px}
.banner div{background:#fff;border:1px solid #ccc;height:100%;display:flex;align-items:center;justify-content:center;font-size:11px;letter-spacing:-.2px;font-weight:700;color:var(--heading);white-space:nowrap}
.seller{left:240px;width:177px;display:flex;align-items:center;justify-content:center;font-size:26px;font-weight:700}
.map{left:439px;top:176px;width:523px;height:292px;border-radius:5px;border:1px solid #ccc;background:linear-gradient(135deg,#ece8df,#e2ddd2)}
.arrow{top:579px;border:5px solid transparent}
.card{top:479px;width:115px;height:214px;border:1px solid #ccc;border-radius:4px;background:#f2f2f2;text-align:center;font-family:Arial,sans-serif}
.card .thumb{margin:5px;height:108px;background:#fff;border:1px solid #ccc}
.card h4{font-size:9px;margin-top:4px;color:#333}
.card p{font-size:8px;line-height:12px;color:#333}
.card hr{border:none;border-top:1px solid #ccc;margin:6px 5px}
.card .price{font-size:11px;font-weight:700;font-family:"Open Sans",sans-serif}
.buy{display:inline-flex;align-items:center;gap:3px;margin-top:4px;background:var(--green);color:#fff;font-size:8px;height:20px;padding:0 7px;border-radius:2px}
.listings{left:439px;top:705px;width:523px;height:320px;background:var(--panel);border:1px solid #ddd;border-radius:4px}
.row{position:absolute;left:8px;width:508px;height:101px;border-bottom:1px solid #ddd}
.row .thumb{position:absolute;left:0;top:8px;width:134px;height:90px;background:#fff;border:1px solid #ccc}
.col{position:absolute;top:4px;height:94px;text-align:center}
.col.sep{border-left:1px solid #ddd}
.label{font-size:9px;font-weight:600;color:#444;margin-top:8px}
.lname{font-size:12px;font-weight:600;color:var(--brand);line-height:17px;margin-top:14px;white-space:nowrap}
.big{font-size:24px;font-weight:700;color:#444;line-height:28px;margin-top:6px}
.small{font-size:9px;font-weight:600;color:#444;line-height:17px}
.loc{font-size:9px;font-weight:600;color:#444;line-height:17px;margin-top:6px}
.cost{font-size:20px;font-weight:700;color:#444;margin-top:16px}
</style>
</head>
<body>
<div class="deco" role="img" aria-label="Shipping container illustration" style="left:156px;top:210px;width:74px;height:330px;border-radius:4px"></div>
<div class="deco" role="img" aria-label="Shipping container illustration" style="left:971px;top:330px;width:129px;height:195px;border-radius:4px"></div>

<div class="abs logo">boxbid.com</div>
<div class="abs toplinks">Create an Account<span>|</span>Login<span>|</span>About BoxBid.com<span>|</span>Contact Us&nbsp; (555) 014-2290</div>

<nav class="abs mainnav">
  <a class="active">20' Shipping Containers</a>
  <a style="left:153px">40' Shipping Containers</a>
  <a style="left:287px">40' High Cube Containers</a>
  <a style="left:428px">Open Top Containers</a>
  <a style="left:552px">How to Buy a Shipping Container</a>
</nav>

<div class="abs search search-input">City, State or Country
  <svg class="abs" style="left:12px;top:6px" width="16" height="16" viewBox="0 0 16 16"><circle cx="9.5" cy="6.5" r="4.5" fill="none" stroke="#7fb8d8" stroke-width="1.6"/><line x1="6" y1="10" x2="2" y2="14" stroke="#7fb8d8" stroke-width="2"/></svg>
</div>
<div class="abs search select" style="left:668px;width:102px">Container Type</div>
<div class="abs search select" style="left:779px;width:70px">Units</div>
<div class="abs search search-btn">SEARCH</div>

<div class="abs content"></div>
<div class="abs divider"></div>

<ul class="abs sidemenu">
  <li>How to Buy Shipping Containers</li><li>New Listings</li><li>News and Articles</li><li>About BoxBid.com</li><li>Container Weight &amp; Dimensions</li><li>BoxBid.com FAQ's</li><li>Shipping Container Terms</li><li>How to Sell Your Containers</li>
</ul>

<div class="abs side-title" style="top:451px">Subscribe to Our Newsletter</div>
<div class="abs newsletter">Enter Email Address<b>Subscribe</b></div>
<div class="abs banner"><div>Container Lock Box Banner</div></div>

<div class="abs side-title" style="top:656px">Featured Sellers</div>
<div class="abs seller" style="top:680px;height:61px;background:#3d5a96;color:#fff">Harborline</div>
<div class="abs seller" style="top:750px;height:76px;background:#e4691c;color:#fff">Tidewater</div>
<div class="abs seller" style="top:834px;height:77px;border:1px solid #ccc;color:var(--navy)">Keelson</div>
<div class="abs seller" style="top:918px;height:77px;border:1px solid #ccc;color:#2f8a3a">Portmark</div>

<div class="abs map" role="img" aria-label="Street map showing the listing location"></div>

<div class="abs arrow" style="left:434px;border-right:7px solid #555;border-left:none"></div>
<div class="abs arrow" style="left:959px;border-left:7px solid #555;border-right:none"></div>

<div class="abs card" style="left:454px"><div class="thumb"></div><h4>Listing Name</h4><p>20' Shipping Container<br>Long Beach, CA</p><hr><div class="price">$ 5140</div><span class="buy"><svg width="10" height="9" viewBox="0 0 10 9"><path d="M0 1h2l1.2 4.5h5L9.5 2H3" fill="none" stroke="#fff" stroke-width="1.2"/><circle cx="4" cy="7.8" r=".9" fill="#fff"/><circle cx="7.5" cy="7.8" r=".9" fill="#fff"/></svg>BUY NOW</span></div>
<div class="abs card" style="left:581px"><div class="thumb"></div><h4>Listing Name</h4><p>20' Shipping Container<br>Long Beach, CA</p><hr><div class="price">$ 5140</div><span class="buy"><svg width="10" height="9" viewBox="0 0 10 9"><path d="M0 1h2l1.2 4.5h5L9.5 2H3" fill="none" stroke="#fff" stroke-width="1.2"/><circle cx="4" cy="7.8" r=".9" fill="#fff"/><circle cx="7.5" cy="7.8" r=".9" fill="#fff"/></svg>BUY NOW</span></div>
<div class="abs card" style="left:709px"><div class="thumb"></div><h4>Listing Name</h4><p>20' Shipping Container<br>Long Beach, CA</p><hr><div class="price">$ 5140</div><span class="buy"><svg width="10" height="9" viewBox="0 0 10 9"><path d="M0 1h2l1.2 4.5h5L9.5 2H3" fill="none" stroke="#fff" stroke-width="1.2"/><circle cx="4" cy="7.8" r=".9" fill="#fff"/><circle cx="7.5" cy="7.8" r=".9" fill="#fff"/></svg>BUY NOW</span></div>
<div class="abs card" style="left:836px"><div class="thumb"></div><h4>Listing Name</h4><p>20' Shipping Container<br>Long Beach, CA</p><hr><div class="price">$ 5140</div><span class="buy"><svg width="10" height="9" viewBox="0 0 10 9"><path d="M0 1h2l1.2 4.5h5L9.5 2H3" fill="none" stroke="#fff" stroke-width="1.2"/><circle cx="4" cy="7.8" r=".9" fill="#fff"/><circle cx="7.5" cy="7.8" r=".9" fill="#fff"/></svg>BUY NOW</span></div>

<div class="abs listings">
  <div class="row" style="top:0">
    <div class="thumb"></div>
    <div class="col" style="left:140px;width:134px"><div class="label">Listing Name</div><div class="lname">40' New One Trip<br>Door on Both Ends</div></div>
    <div class="col sep" style="left:273px;width:80px"><div class="label">Container Type</div><div class="big">40'</div><div class="small">Dry box</div></div>
    <div class="col sep" style="left:353px;width:73px"><div class="label">Location</div><div class="loc">Long Beach /<br>CA, 90802,<br>United States</div></div>
    <div class="col sep" style="left:426px;width:82px"><div class="label">Price</div><div class="cost">$5140</div></div>
  </div>
  <div class="row" style="top:101px">
    <div class="thumb"></div>
    <div class="col" style="left:140px;width:134px"><div class="label">Listing Name</div><div class="lname">40' New One Trip<br>Door on Both Ends</div></div>
    <div class="col sep" style="left:273px;width:80px"><div class="label">Container Type</div><div class="big">40'</div><div class="small">Dry box</div></div>
    <div class="col sep" style="left:353px;width:73px"><div class="label">Location</div><div class="loc">Long Beach /<br>CA, 90802,<br>United States</div></div>
    <div class="col sep" style="left:426px;width:82px"><div class="label">Price</div><div class="cost">$5140</div></div>
  </div>
  <div class="row" style="top:202px">
    <div class="thumb"></div>
    <div class="col" style="left:140px;width:134px"><div class="label">Listing Name</div><div class="lname">40' New One Trip<br>Door on Both Ends</div></div>
    <div class="col sep" style="left:273px;width:80px"><div class="label">Container Type</div><div class="big">40'</div><div class="small">Dry box</div></div>
    <div class="col sep" style="left:353px;width:73px"><div class="label">Location</div><div class="loc">Long Beach /<br>CA, 90802,<br>United States</div></div>
    <div class="col sep" style="left:426px;width:82px"><div class="label">Price</div><div class="cost">$5140</div></div>
  </div>
</div>
</body>
</html>
```